Corvane Project Services - Flyer

Project Breif:
I need a single page A4 Capability Statement, which will be used to market our services to prospective clients, both in print and via email PDF.
It needs to look professional and should incorporate the elements I have uploaded into files, these include:
Capability Statement Text
Corvane Services Company Logo
Additional Logo’s (Tools We Use)
Glimmer Bay Pics can be cut into the page
I have included examples of capability statements as a guide to what i am looking for.
Regards
Derek
Engineering Consulting

```html
<!DOCTYPE html>
<html lang="en">
<head>
<meta charset="utf-8">
<title>Corvane Project Services – Capability Statement</title>
<link rel="stylesheet" href="https://fonts.googleapis.com/css2?family=Michroma&family=Roboto:wght@400;500;700&display=swap">
<style>
:root{
  --blue:#1a7cc6;
  --blue-dark:#0d6cb5;
  --grey-text:#555;
  --dark-text:#2b2b2b;
  --panel:#f5f5f5;
  --backdrop:#636365;
  --white:#fff;
}
*{margin:0;padding:0;box-sizing:border-box}
html,body{width:980px;height:1200px;overflow:hidden;background:var(--backdrop)}
body{font-family:'Roboto',Arial,sans-serif;position:relative}
.page{position:absolute;left:72px;top:9px;width:836px;height:1182px;background:var(--white);overflow:hidden}
.brand{position:absolute;left:62px;top:28px;width:200px;text-align:center}
.brand-mark{width:50px;height:50px;border-radius:50%;background:var(--blue);margin:0 auto 14px}
.brand-name{font-family:'Roboto',Arial,sans-serif;font-weight:700;font-size:14px;color:var(--dark-text);letter-spacing:.5px;line-height:1.25}
.title{position:absolute;right:72px;top:54px;text-align:right;font-family:'Michroma',sans-serif;line-height:1}
.title .t1{display:block;font-size:27px;color:var(--blue)}
.title .t2{display:block;font-size:30px;color:#7b7b7b;margin-top:2px}
.title-bar{position:absolute;left:783px;top:0;width:4px;height:121px;background:var(--blue)}
.hero{position:absolute;left:0;top:159px;width:836px;height:301px;background:linear-gradient(100deg,#cfdde6 0%,#eef3f6 35%,#dfe8ee 60%,#b9cfdf 100%)}
.about{position:absolute;left:0;top:485px;width:407px;height:563px;background:var(--panel);padding:54px 54px 0 67px}
.about .lead{font-size:19px;color:var(--blue);line-height:22px;margin-bottom:22px}
.about p{font-size:17.5px;color:var(--grey-text);line-height:20.5px;margin-bottom:20px}
.services{position:absolute;left:434px;top:505px;width:380px}
.services h2{font-family:'Michroma',sans-serif;font-weight:400;font-size:24px;color:var(--dark-text);border-left:4px solid var(--blue);padding-left:11px;line-height:28px;margin-bottom:12px}
.services h3{font-size:19px;font-weight:700;color:var(--blue);margin:0 0 9px 15px;line-height:22px}
.services ul{list-style:none;margin:0 0 18px 38px}
.services li{font-size:15px;color:var(--dark-text);line-height:20.8px;position:relative;padding-left:14px}
.services li::before{content:"";position:absolute;left:0;top:8px;width:4px;height:4px;border-radius:50%;background:var(--blue)}
.tools{position:absolute;left:40px;top:1075px;width:760px;height:30px;display:flex;justify-content:space-between;align-items:center}
.tool{font-size:14px;font-weight:500;color:#444;display:flex;align-items:center;gap:6px}
.tool .dot{width:10px;height:10px;background:var(--blue)}
.footer{position:absolute;left:0;top:1120px;width:836px;height:62px;background:var(--blue-dark);color:var(--white);display:flex;align-items:center;padding-left:56px}
.contact-person .name{font-size:16px;line-height:18px}
.contact-person .role{font-size:11px}
.contact{display:flex;align-items:center;gap:7px;font-size:14px;height:34px;padding:0 16px}
.contact+.contact{border-left:1px solid rgba(255,255,255,.7)}
.contact.phone{margin-left:54px}
.contact svg{width:20px;height:20px;fill:none;stroke:#fff;stroke-width:1.4}
</style>
</head>
<body>
<div class="page">
  <header>
    <div class="brand">
      <div class="brand-mark"></div>
      <div class="brand-name">CORVANE PROJECT SERVICES</div>
    </div>
    <h1 class="title"><span class="t1">CAPABILITY</span><span class="t2">STATEMENT</span></h1>
    <div class="title-bar"></div>
  </header>

  <div class="hero" role="img" aria-label="Photo of colleagues reviewing printed reports and charts at a desk with pens"></div>

  <section class="about">
    <p class="lead">Corvane Project Services Ltd.is a leading project control consultancy based in Co Cork Ireland</p>
    <p>For over 20 years we have been helping our clients to deliver complex projects and programs throughout mainland Europe.</p>
    <p>We are passionate about empower organisations to achieve their objectives, on time and on budget.</p>
    <p>We are continually innovating, evolving and learning, utilize the latest industry tools and techniques to deliver real value to our clients.</p>
    <p>Our goal is to make successful project delivery more achievable and repeatable.</p>
  </section>

  <section class="services">
    <h2>CORE SERVICES:</h2>
    <h3>PLANNING AND SCHEDULING</h3>
    <ul>
      <li>Tender Planning</li>
      <li>Interactive Planning / Pull Planning</li>
      <li>EPCMV Planning &amp; Scheduling</li>
      <li>Schedule Earned Value Management</li>
      <li>Independent Schedule Quality Assessment</li>
      <li>Schedule Risk Analysis (Monte Carlo)</li>
      <li>Training</li>
    </ul>
    <h3>MANAGEMENT OF RISK</h3>
    <ul>
      <li>Risk Management Policies &amp; Procedures</li>
      <li>Risk Management Strategy</li>
      <li>Risk Registers</li>
      <li>Risk Improvement Planning</li>
      <li>Risk Response and Communication</li>
      <li>Risk Management Training</li>
    </ul>
    <h3>COST CONTROL:</h3>
    <ul>
      <li>Estimating &amp; Forecasting</li>
      <li>Earned Value Analysis</li>
      <li>Progress Reporting</li>
      <li>Cost Risk Analysis</li>
    </ul>
  </section>

  <div class="tools">
    <span class="tool">Plantrix</span>
    <span class="tool"><span class="dot"></span>Taskbase</span>
    <span class="tool">Vesta Planner</span>
    <span class="tool">Waypoint Pro</span>
    <span class="tool">Ledgerly</span>
    <span class="tool">Keenscope</span>
    <span class="tool">Riskwise</span>
  </div>

  <footer class="footer">
    <div class="contact-person">
      <div class="name">Derek Halloran</div>
      <div class="role">Managing Director</div>
    </div>
    <div class="contact phone">
      <svg viewBox="0 0 24 24"><path d="M5 3h4l2 5-2.5 1.5a11 11 0 0 0 6 6L16 13l5 2v4a2 2 0 0 1-2 2A16 16 0 0 1 3 5a2 2 0 0 1 2-2z"/></svg>
      +353 (0)871456290
    </div>
    <div class="contact">
      <svg viewBox="0 0 24 24"><rect x="3" y="6" width="18" height="12"/><path d="M3 6l9 7 9-7"/></svg>
      info@corvaneservices.ie
    </div>
    <div class="contact">
      <svg viewBox="0 0 24 24"><circle cx="12" cy="12" r="9"/><path d="M3 12h18M12 3c3 3 3 15 0 18M12 3c-3 3-3 15 0 18"/></svg>
      www.corvaneservices.ie
    </div>
  </footer>
</div>
</body>
</html>
```